Bag Design For Outdoors Industry

We are a Midwest seed company that is looking for a bag design for our Food Plot Product Line, "Ridgehorn". We are looking for a broad design that will work for several SKUs. Attached is the dieline for 4.5"x9.5"x20.75" bag and specifications for the print company. Also included are the brand standards and our catalog. The bag design should pull the themes and concepts established in the catalog. We will be placing 4"x9" labels on the front and back of the bag (design should have a guide for labels). Front of package will include a clear window to see the product. Use the attached layout PDF for a rough idea of how it should be formatted. The final design should convey the simple brand and overall themes.

Target Market(s)

Outdoor enthusiasts

Industry/Entity Type

Outdoors

Requirements
Must have
• Follow our provided branding, clear window

```html
<!DOCTYPE html>
<html lang="en">
<head>
<meta charset="utf-8">
<title>Ridgehorn Annual Forage Mix Bag</title>
<link rel="stylesheet" href="https://fonts.googleapis.com/css2?family=Montserrat:wght@400;700;800&family=Oswald:wght@400;600&family=Roboto:wght@400;500&family=Roboto+Condensed:wght@400&display=swap">
<style>
  :root {
    --paper: #ffffff;
    --side-dark: #1d1d1d;
    --panel-light: #e5e5e5;
    --ink: #1a1a1a;
    --white: #ffffff;
    --season-orange: #f0a133;
    --seed-light: #c9a26a;
    --seed-dark: #4a3526;
  }
  html, body {
    margin: 0;
    padding: 0;
    width: 1200px;
    height: 883px;
    overflow: hidden;
    background: var(--paper);
  }
  .dieline {
    position: relative;
    width: 1200px;
    height: 883px;
    font-family: "Roboto", sans-serif;
    color: var(--ink);
  }
  .panel {
    position: absolute;
    top: 49px;
    height: 796px;
    overflow: hidden;
  }
  .gusset { width: 172px; background: var(--side-dark); }
  .gusset--left { left: 58px; }
  .gusset--right { left: 596px; }
  .face { width: 366px; background: var(--panel-light); }
  .face--front { left: 230px; }
  .face--back { left: 768px; width: 365px; }

  .gusset__name {
    position: absolute;
    left: 99px;
    top: 390px;
    transform: translate(-50%, -50%) rotate(-90deg);
    font-family: "Montserrat", sans-serif;
    font-weight: 800;
    font-size: 50px;
    letter-spacing: 1px;
    color: var(--white);
    white-space: nowrap;
  }
  .gusset__tagline {
    position: absolute;
    left: 126px;
    top: 253px;
    transform: translate(-50%, -50%) rotate(-90deg);
    font-family: "Montserrat", sans-serif;
    font-weight: 400;
    font-size: 12.5px;
    letter-spacing: 2px;
    color: var(--white);
    white-space: nowrap;
  }

  .front__brand {
    position: absolute;
    left: 0;
    width: 366px;
    top: 76px;
    text-align: center;
    font-family: "Montserrat", sans-serif;
    font-weight: 700;
    font-size: 15px;
    letter-spacing: 0.5px;
    color: var(--ink);
  }
  .front__brand::before {
    content: "";
    display: inline-block;
    width: 9px;
    height: 9px;
    border-radius: 50%;
    background: var(--ink);
    margin-right: 6px;
    vertical-align: 1px;
  }

  .label {
    position: absolute;
    left: 11px;
    top: 168px;
    width: 345px;
    height: 153px;
    background: var(--white);
    text-align: center;
  }
  .label__line {
    position: absolute;
    left: 0;
    width: 100%;
    margin: 0;
  }
  .label__kicker {
    top: 18px;
    font-size: 11px;
    letter-spacing: 5px;
    font-weight: 500;
  }
  .label__title {
    top: 33px;
    font-family: "Oswald", sans-serif;
    font-weight: 600;
    font-size: 23px;
    letter-spacing: 0;
    transform: scaleX(0.92);
  }
  .label__season {
    position: absolute;
    left: 128px;
    top: 68px;
    width: 89px;
    height: 12px;
    background: var(--season-orange);
    color: var(--white);
    font-size: 8px;
    font-weight: 500;
    letter-spacing: 3px;
    line-height: 12px;
  }
  .label__uses {
    position: absolute;
    left: 30px;
    top: 104px;
    width: 283px;
    height: 30px;
    border: 1px solid var(--ink);
    box-sizing: border-box;
  }
  .label__uses-title {
    position: absolute;
    top: -9px;
    left: 50%;
    transform: translateX(-50%);
    background: var(--white);
    padding: 0 7px;
    font-family: "Roboto Condensed", sans-serif;
    font-size: 12px;
    line-height: 14px;
  }
  .label__uses-list {
    margin: 0;
    line-height: 30px;
    font-size: 9.5px;
    letter-spacing: 2px;
  }

  .front__window { position: absolute; left: 0; top: 0; }
  .front__badge {
    position: absolute;
    left: 247px;
    top: 698px;
    width: 70px;
    height: 70px;
    border-radius: 50%;
    background: var(--ink);
  }

  .back__slogan {
    position: absolute;
    left: 0;
    width: 365px;
    top: 247px;
    margin: 0;
    text-align: center;
    font-family: "Roboto Condensed", sans-serif;
    font-size: 18.5px;
    line-height: 32px;
    color: var(--ink);
  }
  .back__label {
    position: absolute;
    left: 10px;
    top: 559px;
    width: 346px;
    height: 153px;
    background: var(--white);
  }
  .back__label-note {
    position: absolute;
    left: 0;
    width: 100%;
    top: 67px;
    margin: 0;
    text-align: center;
    font-family: "Roboto Condensed", sans-serif;
    font-size: 6.5px;
    line-height: 8.4px;
  }
</style>
</head>
<body>
<main class="dieline">

  <section class="panel gusset gusset--left" aria-label="Left gusset">
    <span class="gusset__name">RIDGEHORN</span>
    <span class="gusset__tagline">FOOD PLOT SEED</span>
  </section>

  <section class="panel face face--front" aria-label="Front face">
    <div class="front__brand">RIDGEHORN</div>

    <div class="label">
      <p class="label__line label__kicker">BLENDS &amp; HABITAT</p>
      <h1 class="label__line label__title">ANNUAL FORAGE MIX</h1>
      <span class="label__season">SPRING/FALL</span>
      <div class="label__uses">
        <span class="label__uses-title">Best for</span>
        <p class="label__uses-list">DEER * NEWLY BROKEN GROUND * SCENERY</p>
      </div>
    </div>

    <svg class="front__window" width="366" height="796" viewBox="0 0 366 796" role="img" aria-label="Clear window showing oat and brassica seed mix">
      <defs>
        <linearGradient id="seed-tone" x1="0" y1="0" x2="1" y2="1">
          <stop offset="0" stop-color="var(--seed-light)"/>
          <stop offset="0.55" stop-color="#9b7650"/>
          <stop offset="1" stop-color="var(--seed-dark)"/>
        </linearGradient>
      </defs>
      <polygon points="0,478 366,796 0,796" fill="url(#seed-tone)"/>
    </svg>

    <div class="front__badge" role="img" aria-label="Certification badge"></div>
  </section>

  <section class="panel gusset gusset--right" aria-label="Right gusset">
    <span class="gusset__name">RIDGEHORN</span>
    <span class="gusset__tagline">FOOD PLOT SEED</span>
  </section>

  <section class="panel face face--back" aria-label="Back face">
    <p class="back__slogan">SOURCED PURE.<br>PACKAGED FRESH.<br>SIMPLE BRAND.</p>
    <div class="back__label">
      <p class="back__label-note">MORE INFO IN BLACK TEXT<br>FONT: UNIVERS 57 CONDENSED<br>SIZE:13PT.<br>WHITE BACKGROUND</p>
    </div>
  </section>

</main>
</body>
</html>
```